Business card design for Velvet Harbor

We need business cards designed for our new marketing consulting company, Velvet Harbor. Our services include marketing strategy, go-to-market and launch planning, growth strategy, and execution. We serve medical technology and health technology companies, from startups to well-established growth companies.

The business cards should feel professional, credible, reliable and trustworthy, and should instill confidence. Also bold, creative, and modern.

The design must use the Velvet Harbor logo.

The primary brand color is this orange: #FF5501
A secondary color that you can use is this gray: #282B2D
I would prefer only to use the orange and gray. But if you feel you really need an additional accent color (please use it very sparingly, as little as possible), you can use this blue for small accent purposes: #009FED

Attached are the logo files. The main logo is the one with a little bit of orange on the left and the rest is gray.

The business card should include the following:

Velvet Harbor logo
First name and last name
Title
Email address
Phone number and type (in whatever order looks best for the design
Website (the website does not need to be in the same block as the personal info)

For example:

Nessa Pryle
Founder & Principal
nessa@velvetharbor.com
+1.628.309.4156 mobile (can use "." or spaces in between blocks of numbers)
velvetharbor.com (somewhere on the card, it does not need to be with the personal info; and note that there is no "www." at the beginning)

Note that there will be no address listed on the business card.

Target Market(s)

Executives (CEO, head of marketing, head of sales) at medical technology and health technology companies, mostly in their 40s and older, well-educated, often with advanced degrees. They are strategic thinkers, responsible for budgets, and familiar with P&L. Their comfort with and trust in using outside consultants varies.

Industry/Entity Type

Medical technology and health technology companies.

Contact Information for Business Card

See project description

Font styles to use
Sans Serif

Requirements
Must have
• Logo and see Business card details section above.

```html
<!DOCTYPE html>
<html lang="en">
<head>
<meta charset="utf-8">
<title>Velvet Harbor — Business Card</title>
<link href="https://fonts.googleapis.com/css2?family=Open+Sans:wght@400;600;700&display=swap" rel="stylesheet">
<style>
  :root {
    --backdrop: #222222;
    --card-gray: #282B2D;
    --brand-orange: #F15A24;
    --ink-white: #FFFFFF;
    --shadow: rgba(0, 0, 0, 0.45);
  }
  * { box-sizing: border-box; margin: 0; padding: 0; }
  html, body {
    width: 1200px; height: 780px; overflow: hidden;
    background: var(--backdrop);
    font-family: "Open Sans", Arial, sans-serif;
  }
  .stage {
    width: 1200px; height: 780px;
    display: flex; align-items: center; justify-content: center; gap: 44px;
  }
  .card {
    position: relative;
    width: 540px; height: 309px;
    border-radius: 24px;
    background: var(--card-gray);
    overflow: hidden;
    box-shadow: 0 14px 30px var(--shadow);
  }
  .card-art { position: absolute; inset: 0; width: 100%; height: 100%; }

  .wordmark {
    display: flex; align-items: center; gap: 14px;
  }
  .wordmark-dot {
    width: 16px; height: 16px; border-radius: 50%; flex: none;
    background: var(--brand-orange);
  }
  .wordmark-text {
    color: var(--ink-white);
    font-weight: 700; line-height: 1.05;
    letter-spacing: 0.14em; text-transform: uppercase;
  }

  /* back */
  .back-wordmark { position: absolute; right: 40px; bottom: 48px; }
  .back-wordmark .wordmark-text { font-size: 26px; }

  /* front */
  .front-wordmark { position: absolute; left: 120px; top: 42px; }
  .front-wordmark .wordmark-dot { width: 20px; height: 20px; }
  .front-wordmark .wordmark-text { font-size: 30px; }

  .identity { position: absolute; left: 64px; top: 160px; }
  .person-name { font-weight: 700; font-size: 30px; line-height: 1.05; color: var(--ink-white); }
  .person-name .first { color: var(--brand-orange); }
  .person-title { font-size: 14px; color: var(--ink-white); margin-top: 3px; }
  .divider {
    position: absolute; left: 268px; top: 120px;
    width: 1px; height: 92px; background: var(--brand-orange);
  }
  .contacts {
    position: absolute; left: 288px; top: 126px;
    list-style: none; display: flex; flex-direction: column; gap: 8px;
  }
  .contact-line {
    display: flex; align-items: center; gap: 8px;
    color: var(--ink-white); font-size: 13.5px; line-height: 1.2;
  }
  .contact-icon { width: 14px; height: 14px; flex: none; }
  .website {
    position: absolute; right: 130px; bottom: 26px;
    color: var(--ink-white); font-size: 14px; font-weight: 600;
  }
</style>
</head>
<body>
<main class="stage">

  <section class="card card-back" aria-label="Card back">
    <div class="wordmark back-wordmark">
      <span class="wordmark-dot"></span>
      <span class="wordmark-text">Velvet<br>Harbor</span>
    </div>
  </section>

  <section class="card card-front" aria-label="Card front">
    <svg class="card-art" viewBox="0 0 540 309" preserveAspectRatio="none" aria-hidden="true">
      <path class="orange-band" d="M0 240 Q320 256 540 172 L540 309 L0 309 Z" fill="var(--brand-orange)"/>
      <path class="swoosh" d="M22 236 Q320 244 528 156 Q320 250 22 236 Z" fill="var(--ink-white)" stroke="var(--ink-white)" stroke-width="1.2"/>
    </svg>

    <div class="wordmark front-wordmark">
      <span class="wordmark-dot"></span>
      <span class="wordmark-text">Velvet<br>Harbor</span>
    </div>

    <div class="identity">
      <p class="person-name"><span class="first">Nessa</span> Pryle</p>
      <p class="person-title">Founder &amp; Principal</p>
    </div>

    <span class="divider"></span>

    <ul class="contacts">
      <li class="contact-line">
        <svg class="contact-icon" viewBox="0 0 24 24" aria-hidden="true"><path fill="var(--brand-orange)" d="M6.6 10.8a15.1 15.1 0 0 0 6.6 6.6l2.2-2.2a1 1 0 0 1 1-.25 11.4 11.4 0 0 0 3.6.57 1 1 0 0 1 1 1V20a1 1 0 0 1-1 1A17 17 0 0 1 3 4a1 1 0 0 1 1-1h3.5a1 1 0 0 1 1 1c0 1.25.2 2.45.57 3.6a1 1 0 0 1-.25 1z"/></svg>
        (628) 309-4156
      </li>
      <li class="contact-line">
        <svg class="contact-icon" viewBox="0 0 24 24" aria-hidden="true"><path fill="var(--brand-orange)" d="M3 5h18a1 1 0 0 1 1 1v12a1 1 0 0 1-1 1H3a1 1 0 0 1-1-1V6a1 1 0 0 1 1-1zm9 7.5L4 7.4V8l8 5 8-5v-.6z"/></svg>
        nessa@velvetharbor.com
      </li>
    </ul>

    <p class="website">velvetharbor.com</p>
  </section>

</main>
</body>
</html>
```